Plumber needs a business card

I need a new business card for my plumbing business. I dont have a logo at the moment but I want business cards that are simple but very professional. I want to look like
Name: Mitch Dorley
Address: (just make one up)
Phone: 0455 318 726
Email: mitch@dorleymail.com
Colors to use:
Blacks, blues, silvers

```html
<!DOCTYPE html>
<html lang="en">
<head>
<meta charset="utf-8">
<title>Mitch Dorley – Plumbing Business Card</title>
<link rel="stylesheet" href="https://fonts.googleapis.com/css2?family=Lato:wght@400;700;900&display=swap">
<style>
  :root {
    --backdrop: #2b2b2b;
    --card: #ffffff;
    --brand-blue: #0f4c8a;
    --brand-blue-light: #4b86c4;
    --swoosh-black: #1c1d21;
    --silver: #b9bec6;
    --text-grey: #3d3d3d;
  }
  html, body {
    margin: 0;
    padding: 0;
    width: 1200px;
    height: 848px;
    overflow: hidden;
    background: var(--backdrop);
    font-family: "Lato", Arial, sans-serif;
  }
  .business-card {
    position: absolute;
    left: 249px;
    top: 224px;
    width: 701px;
    height: 400px;
    background: var(--card);
    border-radius: 20px;
    overflow: hidden;
    box-shadow: 0 6px 18px rgba(0,0,0,0.45);
  }
  .edge-tab {
    position: absolute;
    left: -6px;
    top: 149px;
    width: 16px;
    height: 47px;
    background: var(--brand-blue);
    border-radius: 4px;
  }
  .identity {
    position: absolute;
    left: 59px;
    top: 150px;
  }
  .identity__name {
    margin: 0;
    font-size: 22px;
    font-weight: 900;
    color: var(--brand-blue);
    line-height: 26px;
  }
  .identity__role {
    margin: 0;
    font-size: 16px;
    color: var(--text-grey);
    line-height: 20px;
    white-space: nowrap;
  }
  .identity-rule {
    position: absolute;
    left: 198px;
    right: 0;
    top: 185px;
    height: 2px;
    background: var(--brand-blue);
  }
  .contact-list {
    position: absolute;
    left: 59px;
    top: 239px;
    margin: 0;
    padding: 0;
    list-style: none;
    font-size: 16px;
    color: var(--text-grey);
    line-height: 20px;
  }
  .contact-list li {
    display: flex;
    align-items: center;
    gap: 8px;
  }
  .contact-list svg {
    width: 15px;
    height: 15px;
    fill: var(--brand-blue);
  }
  .address {
    position: absolute;
    right: 57px;
    top: 258px;
    margin: 0;
    font-style: normal;
    text-align: right;
    font-size: 16px;
    line-height: 20px;
    color: var(--text-grey);
  }
  .bottom-wave {
    position: absolute;
    left: 0;
    top: 0;
    width: 701px;
    height: 400px;
  }
</style>
</head>
<body>
  <div class="business-card">
    <div class="edge-tab"></div>

    <div class="identity">
      <p class="identity__name">Mitch Dorley</p>
      <p class="identity__role">Plumbing Business</p>
    </div>
    <div class="identity-rule"></div>

    <ul class="contact-list">
      <li>
        <svg viewBox="0 0 16 16" aria-hidden="true"><rect x="4" y="1" width="8" height="14" rx="1.5"/><rect x="5.5" y="3" width="5" height="5" fill="#fff"/></svg>
        000.000.0000
      </li>
      <li>
        <svg viewBox="0 0 16 16" aria-hidden="true"><path d="M4 1 L6.5 4 L5 6 C6 8.5 7.5 10 10 11 L12 9.5 L15 12 L13 15 C7 14 2 9 1 3 Z"/></svg>
        0455 318 726
      </li>
      <li>
        <svg viewBox="0 0 16 16" aria-hidden="true"><path d="M1 3 H15 V13 H1 Z M2 4 L8 9 L14 4 Z" fill-rule="evenodd"/></svg>
        mitch@dorleymail.com
      </li>
    </ul>

    <address class="address">
      14 Harbour Lane, PO Box 2281<br>
      Newcastle NSW 2300
    </address>

    <svg class="bottom-wave" viewBox="0 0 701 400" aria-hidden="true">
      <defs>
        <linearGradient id="blueSheen" x1="0" y1="0" x2="1" y2="0">
          <stop offset="0" stop-color="var(--brand-blue-light)"/>
          <stop offset="0.35" stop-color="var(--brand-blue)"/>
        </linearGradient>
      </defs>
      <path d="M170 370 C260 388 330 386 400 384 C520 380 620 362 701 342 L701 362 C620 374 520 385 400 389 C320 391 250 386 170 370 Z" fill="var(--swoosh-black)"/>
      <path d="M0 344 C150 366 250 390 360 389 C500 388 620 374 701 364 L701 400 L0 400 Z" fill="url(#blueSheen)"/>
      <path d="M200 378 C260 388 300 390 360 389 C500 388 620 374 701 364" fill="none" stroke="var(--silver)" stroke-width="2"/>
    </svg>
  </div>
</body>
</html>
```